Need Eye Catching For Sale By Owner Signs

In need of a Eye Catching For Sale By Owner Sign design. I plan on using the sign to market buildings and raw land that I own. The design should be able to scale to different rectangular dimensions for example a yard stake sign or a large 4' x 6' sign to be tacked to plywood. The design should have a dead space near the bottom that I can insert more detail information into at a later time.

The main tag line "For Sale By Owner" and the contact number "318-562-4097" needs to be easily be read from a distance.

```html
<!DOCTYPE html>
<html lang="en">
<head>
<meta charset="utf-8">
<title>For Sale By Owner Sign</title>
<link href="https://fonts.googleapis.com/css2?family=Arimo:wght@400;700&display=swap" rel="stylesheet">
<style>
  :root {
    --page-bg: #e9ebee;
    --sign-blue: #2f64ad;
    --sign-white: #ffffff;
    --ink-black: #111111;
  }
  html, body {
    margin: 0;
    padding: 0;
    width: 1200px;
    height: 1000px;
    overflow: hidden;
    background: var(--page-bg);
  }
  .canvas {
    position: relative;
    width: 1200px;
    height: 1000px;
  }
  .sale-sign {
    position: absolute;
    left: 100px;
    top: 176px;
    width: 1000px;
    height: 648px;
    box-shadow: 0 6px 18px rgba(0,0,0,0.18);
  }
  .sale-sign svg {
    display: block;
    font-family: "Arimo", Arial, Helvetica, sans-serif;
  }
  .sign-for { font-size: 84px; font-weight: 400; fill: var(--sign-white); }
  .sign-sale { font-size: 250px; font-weight: 700; fill: var(--sign-white); }
  .sign-by-owner { font-size: 72px; font-weight: 400; fill: var(--sign-white); letter-spacing: 12px; }
  .sign-phone { font-size: 124px; font-weight: 700; fill: var(--ink-black); letter-spacing: 8px; }
</style>
</head>
<body>
<main class="canvas">
  <div class="sale-sign">
    <svg width="1000" height="648" viewBox="0 0 1000 648" xmlns="http://www.w3.org/2000/svg">
      <rect class="sign-border" x="0" y="0" width="1000" height="648" fill="var(--sign-white)"/>
      <rect class="sign-panel" x="18" y="18" width="964" height="612" fill="var(--sign-blue)"/>
      <text class="sign-for" transform="translate(174 216) rotate(-90)">FOR</text>
      <text class="sign-sale" x="196" y="262" textLength="658" lengthAdjust="spacingAndGlyphs">SALE</text>
      <text class="sign-by-owner" x="532" y="350" text-anchor="middle">BY OWNER</text>
      <rect class="phone-band" x="46" y="362" width="912" height="136" fill="var(--sign-white)"/>
      <text class="sign-phone" x="502" y="475" text-anchor="middle" textLength="880" lengthAdjust="spacingAndGlyphs">318-562-4097</text>
    </svg>
  </div>
</main>
</body>
</html>
```